Professional Consulting Firm Business Card Design

We need a business card design for a new professional consulting firm that specializes in petroleum, health, and financial consulting. We need a design that is trendy but elegant, and one that would make a vantage 300 executive feel comfortable using our services. I have attached a logo that needs to be used in the design. I have also attached a photo of a card design that I like.

On the card we need a place for employee name, title, email address, fax number, phone number, mailing address, and website address.

Industry/Entity Type

Financial

Contact Information for Business Card

see attached

Font styles to use
Other font styles liked:
• Calibri or your choice

Requirements
Must have
• style
Nice to have
• texture, rounded edges
Should not have
• no solid black cards but black may be used

```html
<!DOCTYPE html>
<html lang="en">
<head>
<meta charset="UTF-8">
<title>Kestrel Advisory – Business Card</title>
<link href="https://fonts.googleapis.com/css2?family=Lato:wght@300;400;700&display=swap" rel="stylesheet">
<style>
  :root {
    --backdrop: #2a2a2b;
    --card: #1d1e20;
    --card-edge: #151617;
    --brand-blue: #1f5fa6;
    --label-blue: #2a6fbf;
    --title-blue: #6d9fd6;
    --ink-light: #f2f3f5;
    --rule: #4a4d52;
  }
  * { margin: 0; padding: 0; box-sizing: border-box; }
  html, body {
    width: 1200px; height: 900px; overflow: hidden;
    background: var(--backdrop);
    font-family: "Lato", Calibri, sans-serif;
  }
  .stage {
    position: relative; width: 1200px; height: 900px;
    display: flex; align-items: center; justify-content: center; gap: 60px;
  }
  .card {
    position: relative; width: 500px; height: 286px;
    border-radius: 22px;
    background: radial-gradient(ellipse at 30% 30%, #26282b 0%, var(--card) 55%, var(--card-edge) 100%);
    box-shadow: 0 10px 30px rgba(0,0,0,.35);
    overflow: hidden;
  }
  .brand-square { display: block; flex: none; background: var(--brand-blue); }

  /* front side */
  .card-front .brand-mark {
    position: absolute; left: 30px; top: 120px;
    display: flex; align-items: center; gap: 10px;
    color: var(--brand-blue); font-weight: 700; font-size: 38px; line-height: 1;
  }
  .card-front .brand-square { width: 16px; height: 16px; }
  .card-front .divider {
    position: absolute; left: 236px; top: 50px; width: 1px; height: 190px;
    background: var(--rule);
  }
  .contact-block { position: absolute; left: 252px; top: 48px; color: var(--ink-light); }
  .person-name { color: var(--label-blue); font-size: 19px; font-weight: 400; line-height: 1.2; }
  .person-title { color: var(--title-blue); font-size: 13.5px; margin-top: 2px; }
  .address { font-size: 14px; line-height: 1.3; margin-top: 12px; }
  .contact-lines { list-style: none; font-size: 14px; line-height: 1.35; margin-top: 12px; }
  .contact-lines .label { color: var(--label-blue); display: inline-block; width: 16px; }

  /* back side */
  .card-back .brand-lockup {
    position: absolute; inset: 0;
    display: flex; align-items: center; justify-content: center; gap: 16px;
  }
  .card-back .brand-square { width: 22px; height: 22px; }
  .card-back .divider { width: 1px; height: 76px; background: var(--rule); }
  .wordmark { display: flex; flex-direction: column; gap: 4px; }
  .wordmark-name {
    color: var(--ink-light); font-weight: 300; font-size: 28px;
    letter-spacing: 1.5px; line-height: 1;
  }
  .wordmark-tagline {
    color: var(--label-blue); font-weight: 400; font-size: 7.5px;
    letter-spacing: 0.6px; text-transform: uppercase;
  }
</style>
</head>
<body>
  <main class="stage">
    <section class="card card-front" aria-label="Card front">
      <div class="brand-mark"><span class="brand-square"></span>Kestrel</div>
      <div class="divider"></div>
      <div class="contact-block">
        <h1 class="person-name">Daniel Harrow</h1>
        <p class="person-title">Managing Director</p>
        <p class="address">48 Linden Quay Road<br>Northbay, 204781.</p>
        <ul class="contact-lines">
          <li><span class="label">T:</span>031-550 274 918</li>
          <li><span class="label">F:</span>031-550 274 919</li>
          <li><span class="label">E:</span>hello@kestreladv.com</li>
          <li><span class="label">W:</span>www.kestreladv.com</li>
        </ul>
      </div>
    </section>
    <section class="card card-back" aria-label="Card back">
      <div class="brand-lockup">
        <span class="brand-square"></span>
        <span class="divider"></span>
        <div class="wordmark">
          <span class="wordmark-name">KESTREL ADVISORY</span>
          <span class="wordmark-tagline">Health, safety and financial consulting services</span>
        </div>
      </div>
    </section>
  </main>
</body>
</html>
```